A year in review booklet 12 page square mini booklet

a 12 page (including front and back cover) booklet 4.75 inches square.
Front Cover page (page 1)
Something that says WLGTC 2018 ministry year in review or something like that
Image of baptism/missions/etc
Intro Letter from Gordon (page 2) (text to be filled in later)
His headshot image (uploaded)
Quick note about year end giving (to be filled in later)
Sermon Listens (page 3)
Total # of sermon listens at the top (5800)
headphone icon
key at the bottom that says "headphone icon = X listens)
Try to fill most of the page with icons
Lantern Effort Houses Visited (pages 4 & 5)
Total # of houses visited at the top (23,899)
house icon
key at the bottom that says "house icon = 50? houses)
Babies Saved (page 6)
Total # of babies at the top (265)
baby icon
no key at the bottom make every baby = 1 icon
Tons of food served at Whitcombe Outreach (page 7)
Total # of food distributed at the top (500 tons)
bread loaf icon
key at the bottom that says "bread icon = 1 ton, 1000 lbs?, 100 lbs?)
Mission Trips Taken (pages 8&9)
Total # of mission trips taken at the top (11 trips)
airplane icon

Salvations (page 10)
Total # of salvations at the top (150 salvations)
cross icon
no key at the bottom make every salvation = 1 icon
Baptisms (page 11)
Total # of baptisms at the top 22
water droplet
no key at the bottom make every baptism = 1 icon

Back Cover page (page 12)
Give online shortlink (filled in later)
Give through month of December info

Target Market(s)

Church Congregation

Requirements
Must have
• Good graphics

```html
<!DOCTYPE html>
<html lang="en">
<head>
<meta charset="utf-8">
<title>Message from Pastor Gordon – Page 2</title>
<link rel="stylesheet" href="https://fonts.googleapis.com/css2?family=Montserrat:wght@400;700&family=Crimson+Pro:wght@400&display=swap">
<style>
  :root {
    --navy: #1b3866;
    --periwinkle: #9aa3c6;
    --ink: #231f20;
    --body-ink: #1f1f1f;
    --muted: #8a8a8a;
    --paper: #ffffff;
  }
  * { box-sizing: border-box; margin: 0; padding: 0; }
  html, body { width: 1200px; height: 1200px; overflow: hidden; background: var(--paper); }
  .page { position: relative; width: 1200px; height: 1200px; background: var(--paper); font-family: "Montserrat", Arial, sans-serif; }

  .portrait-frame { position: absolute; left: 0; top: 0; width: 512px; height: 528px; }

  .pastor-card { position: absolute; left: 101px; top: 536px; }
  .pastor-name { font-weight: 700; font-size: 27px; color: var(--ink); letter-spacing: 0.3px; }
  .pastor-role { font-size: 22px; color: var(--ink); margin-top: 8px; }

  .contact-list { list-style: none; margin-top: 36px; }
  .contact-item { display: flex; align-items: center; height: 57px; font-size: 24px; color: var(--ink); letter-spacing: 0.5px; }
  .contact-icon { width: 26px; height: 26px; margin-right: 22px; flex: none; }

  .letter { position: absolute; left: 544px; top: 96px; width: 540px; }
  .letter-title { font-weight: 700; font-size: 32px; color: var(--navy); letter-spacing: 0.2px; }
  .letter-body { margin-top: 20px; height: 880px; overflow: hidden; font-family: "Crimson Pro", Georgia, serif; font-size: 27.5px; line-height: 42px; color: var(--body-ink); hyphens: auto; }
  .letter-body p + p { margin-top: 32px; }

  .page-number { position: absolute; left: 30px; top: 1105px; font-weight: 700; font-size: 66px; color: var(--periwinkle); }
  .church-name { position: absolute; left: 544px; top: 1145px; font-size: 22.5px; color: var(--muted); letter-spacing: 0.6px; text-transform: uppercase; white-space: nowrap; }
</style>
</head>
<body>
<main class="page">
  <svg class="portrait-frame" viewBox="0 0 640 660" aria-hidden="false">
    <defs>
      <clipPath id="top-half"><rect x="0" y="0" width="565" height="362"/></clipPath>
      <clipPath id="bottom-half"><rect x="0" y="362" width="565" height="300"/></clipPath>
      <linearGradient id="portrait-tones" x1="0" y1="0" x2="1" y2="1">
        <stop offset="0" stop-color="#3f6a2c"/>
        <stop offset="0.45" stop-color="#c79a7e"/>
        <stop offset="0.8" stop-color="#b9cde6"/>
        <stop offset="1" stop-color="#27421c"/>
      </linearGradient>
    </defs>
    <ellipse cx="200" cy="362" rx="458" ry="276" fill="var(--navy)" clip-path="url(#top-half)"/>
    <ellipse cx="200" cy="362" rx="458" ry="282" fill="var(--periwinkle)" clip-path="url(#bottom-half)"/>
    <ellipse cx="200" cy="362" rx="432" ry="250" fill="var(--paper)"/>
    <ellipse cx="200" cy="362" rx="422" ry="240" fill="url(#portrait-tones)" role="img" aria-label="Headshot photo of Pastor Gordon Hale smiling outdoors in front of green hedges"/>
  </svg>

  <section class="pastor-card">
    <h2 class="pastor-name">Gordon Hale</h2>
    <p class="pastor-role">Sr. Pastor</p>
    <ul class="contact-list">
      <li class="contact-item">
        <svg class="contact-icon" viewBox="0 0 26 26"><rect x="2" y="5" width="22" height="16" rx="2" fill="none" stroke="var(--periwinkle)" stroke-width="2.4"/><path d="M3 7l10 8 10-8" fill="none" stroke="var(--periwinkle)" stroke-width="2.4"/></svg>
        ghale@wlgtc.com
      </li>
      <li class="contact-item">
        <svg class="contact-icon" viewBox="0 0 26 26"><circle cx="13" cy="13" r="10" fill="var(--periwinkle)"/></svg>
        @gordonhale
      </li>
      <li class="contact-item">
        <svg class="contact-icon" viewBox="0 0 26 26"><rect x="3" y="3" width="20" height="20" fill="var(--periwinkle)"/></svg>
        /ghaleWLGTC
      </li>
      <li class="contact-item">
        <svg class="contact-icon" viewBox="0 0 26 26"><circle cx="13" cy="13" r="10.5" fill="none" stroke="var(--periwinkle)" stroke-width="2.4"/><path d="M7.5 13.5l11-5-5 11-1.5-4.5z" fill="var(--periwinkle)"/></svg>
        www.gordonhale.com
      </li>
    </ul>
  </section>

  <article class="letter">
    <h1 class="letter-title">Message from Pastor Gordon</h1>
    <div class="letter-body" lang="la">
      <p>Lorem ipsum dolor sit amet, consectetur adipiscing elit. Nulla quis odio orci. Aenean vitae sodales libero, id tempor dolor. Curabitur tristique pellentesque efficitur. Integer sed nisi vitae nisl lobortis tincidunt in a sapien. Aliquam dictum ut arcu eu pretium. Sed faucibus mi in scelerisque auctor. Nullam ligula nunc, mattis et turpis id, dictum fermentum ligula. In id pulvinar tortor, eget faucibus neque. Nullam sem erat, maximus nec elit nec, efficitur vehicula turpis.</p>
      <p>Proin bibendum enim eget lacus lobortis accumsan dictum vel velit. Aenean laoreet vulputate erat, at viverra dolor gravida sit amet. Quisque luctus semper eleifend. Morbi elementum hendrerit nisl laoreet volutpat. Etiam eget urna eu mi ornare porta. Vestibulum semper erat mauris, at facilisis nunc faucibus a. Morbi fermentum mollis sapien ultrices sagittis. Quisque pretium massa quis justo porttitor luctus. Morbi dictum ut dolor</p>
    </div>
  </article>

  <div class="page-number">2</div>
  <footer class="church-name">West Lake Grace Tabernacle Church</footer>
</main>
</body>
</html>
```